Zielgruppe
Ich bin Selfpublisher und meine Zielgruppe sind vor allem Erwachsene, die sowohl Science Fantasy wie auch Fantasy Thriller mögen oder ähnliche gemischte Subgenres.
Aufgabenstellung
Ich suche ein Ebook- und Taschenbuchcover für Borvex Lumina und ich brauche ein Ebook-Cover für Quendra-Verbund (Dateianforderung für Quendra: .jpg- oder jepg-Datei, mindestens 1600 Pixel, RPG-Farbraum, maximale Dateigröße 5 MB)
Taschenbuchformat:
Breite: 15,24 cm
Höhe: 22,86 cm
Seitenzahl: 721 Seiten
Das ist das erste Buch einer Trilogie.
Autor: Konrad Weidelbach
Titel: Die Hüterin der Gläsernen Küste (dieser Titel bitte groß darstellen oder hervorheben)
Untertitel: Die Chronik der Schweigenden Herolde I (klein unter dem Titel und mit römischer Zahl)
Als Cover schweben mir zwei Varianten vor:
Variante 1:
Am Horizont hinter Bergen erscheint eine saphirblaue Sonne, so als wäre sie bei der Dämmerung steckengeblieben. Jedoch will ich sie nicht mit blauen Strahlen, sondern als gigantische blaue Feuerkugel, so als wäre die Sonne dem Planeten nähergekommen und würde sie gleich verschlingen. Unter der Sonne eine Großstadt, aus der Rauchsäulen und vielleicht einzelne blaue Flammen aufsteigen, so als würde sie überfallen werden, aber ihre Angreifer sind nicht zu sehen. Da es sich dabei um eine fiktive Welt handelt, sollte die Stadt keine Merkmale von bekannten Städte der Erde haben. Am besten wäre eine Stadt im Stile der 1920er oder des späten 19. Jahrhundert.
Variante 2:
Genau wie die 1. Variante, nur dass statt eine brennende Stadt ein Mann am Fuße des Berges steht. Der Mann trägt einen schwarzen Umhang mit Ärmeln und Kapuze. Sein Gesicht ist durch eine metallische Maske verborgen, der nur einen Sehschlitz hat. Seine Hände sind übersät mit Schnittnarben, als hätte er in einen Dornenbusch gegriffen und in seiner Hand hält er etwas, was goldig aufleuchtet wie eine kleine Sonne und seine Maske aufschimmern lässt, jedoch ist nicht zu sehen, was er in der Hand hält.
Welche der beiden Varianten ihr gestaltet oder für euch machbarer ist, überlasse ich ganz euch. Ich mag ..

```html
<!DOCTYPE html>
<html lang="de">
<head>
<meta charset="utf-8">
<title>Rückseite – Coshia, Norderde</title>
<link rel="stylesheet" href="https://fonts.googleapis.com/css2?family=Federant&family=Arimo:wght@400&display=swap">
<style>
  :root {
    --sky-black: #020305;
    --sky-deep: #07101a;
    --mist-blue: #1d4a66;
    --ridge-blue: #163a52;
    --ground-dark: #06121d;
    --text-white: #f4f6f8;
  }
  html, body {
    margin: 0;
    padding: 0;
    width: 800px;
    height: 1200px;
    overflow: hidden;
    background: var(--sky-black);
  }
  .back-cover {
    position: relative;
    width: 800px;
    height: 1200px;
    overflow: hidden;
    color: var(--text-white);
  }
  .night-landscape {
    position: absolute;
    inset: 0;
    background:
      radial-gradient(ellipse 60% 18% at 60% 20%, rgba(60, 90, 120, 0.25), transparent 70%),
      radial-gradient(circle at 87% 49%, rgba(90, 170, 255, 0.55) 0, rgba(40, 110, 200, 0.18) 18px, transparent 60px),
      linear-gradient(180deg,
        var(--sky-black) 0%,
        var(--sky-deep) 40%,
        var(--ridge-blue) 52%,
        var(--mist-blue) 62%,
        #163b55 72%,
        var(--ground-dark) 88%,
        #040b12 100%);
  }
  .setting {
    position: absolute;
    left: 93px;
    top: 98px;
    margin: 0;
    font-family: "Federant", serif;
    font-weight: 400;
    font-size: 22px;
    line-height: 30px;
    letter-spacing: 0.5px;
  }
  .setting .place { display: block; text-transform: uppercase; }
  .setting .era { display: block; }
  .blurb {
    position: absolute;
    left: 93px;
    top: 181px;
    width: 619px;
    font-family: "Arimo", Arial, sans-serif;
    font-size: 16px;
    line-height: 28.2px;
    text-align: justify;
    hyphens: auto;
  }
  .blurb p { margin: 0; }
  .blurb p + p.section { margin-top: 28.2px; }
  .age-rating {
    position: absolute;
    left: 93px;
    top: 1112px;
    margin: 0;
    font-family: "Arimo", Arial, sans-serif;
    font-size: 14px;
  }
</style>
</head>
<body>
<main class="back-cover">
  <div class="night-landscape" role="img" aria-label="Nächtliche Landschaft mit Sternenhimmel, blau schimmernden Bergen im Nebel und dunklem Grasland"></div>

  <h2 class="setting">
    <span class="place">Coshia, Norderde</span>
    <span class="era">1883 des Dritten Zeitalters</span>
  </h2>

  <section class="blurb">
    <p>Der Schattenweltkrieg verwüstete die Welt Coshia und hätte beinahe alles Leben ausgelöscht. Mittlerweile hat sich die Welt davon erholt und die Schattenmeister gelten seit Jahrtausende als ausgestorben. Aber jetzt taucht ein maskierter Magier auf, der ebenfalls die Künste des Dunklen Pfades beherrscht. Er begehrt das Amulett von Lord Mardon, dem König der Schattenmeister, der damals den Schattenweltkrieg begann.</p>
    <p>Die Drei Kreise befürchten nun, dass der maskierte Magier ein Schattenmeister ist, der das Werk von Lord Mardon vollenden will.</p>
    <p class="section">Um den maskierten Magier zu finden, wird der frustrierte Polizist Beauregard Baine, die lebensfrohe Kopfgeldjägerin Lea Fross und die überhebliche elbische Wächterin Makina Varian beauftragt. Eigentlich will Baine nur herausfinden, warum er in seinen Albträumen immer wieder denselben brutalen Mord begeht und woher die Brandnarbe auf seiner Hand stammt.</p>
    <p>Bei ihrer Suche nach dem vermeitlichen Schattenmeister geraten die ungleichen Gefährten in ein tödliches Netz aus Lügen und Verrat.</p>
  </section>

  <p class="age-rating">Altersempfehlung: ab 16 Jahren</p>
</main>
</body>
</html>
```